The Founder Crossroads Book Cover

I need a Book Cover Design for a new book:
Title - "The Founder Crossroads"
Subtitle - "Lessons No Classroom Ever Gives You"
Author - "Marcus Halden"

Target Market(s)

Entrepreneur's and Small Business Owners

Industry/Entity Type

Entrepreneur

Font styles to use
Sans Serif

Requirements
Must have
• The branding colors should match our website (Black and accent color: #FBBC05)
• http://FounderCrossroads.example
• Secondary Subtile (top bar) on front of cover - "A Documentary"
• Back Cover: Brief description, author photo, and the ISBN Number
Nice to have
• A Detour Sign with the word "Detour" on it (or a sign with a "squiggly" line example) ... or a type of image that is on the bottom of Home page of website (road in wilderness).

```html
<!DOCTYPE html>
<html lang="en">
<head>
<meta charset="UTF-8">
<title>The Founder Crossroads – Book Cover</title>
<link rel="stylesheet" href="https://fonts.googleapis.com/css2?family=Oswald:wght@700&family=Montserrat:wght@800&family=Signika:wght@300&family=Roboto:wght@400&display=swap">
<style>
  :root {
    --ink: #1c1a17;
    --white: #ffffff;
    --sky-top: #f0c82a;
    --sky-mid: #f3dc5a;
    --haze: #efe2b8;
    --sea: #4f9fb8;
    --sea-warm: #c9a7a4;
    --hill: #a0532c;
    --land: #7a5030;
    --scrub: #3e3a22;
    --arrow-a: #fbbc05;
    --arrow-b: #d9780e;
  }
  * { margin: 0; padding: 0; box-sizing: border-box; }
  html, body { width: 800px; height: 1200px; overflow: hidden; background: #fff; }
  .cover { position: relative; width: 800px; height: 1200px; overflow: hidden; }

  .cover-scene {
    position: absolute; inset: 0;
    background:
      radial-gradient(ellipse 420px 160px at 70% 12%, rgba(255,248,200,0.55), transparent 70%),
      radial-gradient(ellipse 360px 140px at 15% 30%, rgba(255,250,190,0.5), transparent 70%),
      radial-gradient(ellipse 460px 120px at 60% 45%, rgba(200,150,40,0.35), transparent 70%),
      linear-gradient(to right, rgba(60,150,185,0.55) 0%, rgba(120,170,190,0.2) 55%, rgba(210,160,170,0.45) 100%) 0 660px / 800px 180px no-repeat,
      radial-gradient(ellipse 520px 90px at 60% 86%, rgba(110,100,90,0.45), transparent 70%),
      linear-gradient(to bottom,
        var(--sky-top) 0%, #f5d648 20%, var(--sky-mid) 38%, #ecd27a 48%,
        var(--haze) 55%, #d9d4c2 55.5%, var(--sea) 58%, #7fb2c2 64%,
        var(--sea-warm) 68%, var(--hill) 71%, #8f5a34 76%,
        var(--land) 82%, #5d5030 88%, var(--scrub) 94%, #2f2a1a 100%);
  }

  .kicker {
    position: absolute; top: 22px; left: 0; width: 813px; text-align: center;
    font-family: "Roboto", sans-serif; font-size: 22px; letter-spacing: 13px;
    color: var(--ink);
  }

  .title-arrow { position: absolute; left: 0; top: 0; }

  .title-line {
    position: absolute; left: 68px;
    font-family: "Oswald", sans-serif; font-weight: 700; color: var(--ink);
    line-height: 1; text-transform: uppercase; white-space: nowrap;
  }
  .title-the { top: 62px; font-size: 42px; }
  .title-founder { top: 111px; font-size: 68px; }
  .title-crossroads { top: 185px; font-size: 100px; letter-spacing: -1px; color: var(--white); }

  .subtitle {
    position: absolute; left: 70px; top: 333px;
    font-family: "Signika", sans-serif; font-weight: 300;
    font-size: 36px; line-height: 45px; color: var(--ink);
  }

  .author {
    position: absolute; left: 0; width: 800px; top: 1098px; text-align: center;
    font-family: "Montserrat", sans-serif; font-weight: 800; font-size: 66px;
    line-height: 1; color: var(--white); letter-spacing: 1px; white-space: nowrap;
  }
</style>
</head>
<body>
<main class="cover">
  <div class="cover-scene" role="img" aria-label="Golden cloudy sky over the ocean with a winding coastal road lit by car light trails through brown hills"></div>

  <p class="kicker">A Documentary</p>

  <svg class="title-arrow" width="800" height="400" viewBox="0 0 800 400" aria-hidden="true">
    <defs>
      <linearGradient id="arrowFill" x1="0" y1="0" x2="1" y2="1">
        <stop offset="0" stop-color="#fbbc05"/>
        <stop offset="1" stop-color="#d9780e"/>
      </linearGradient>
    </defs>
    <polygon points="64,178 591,178 591,129 761,240 591,351 591,296 64,296"
             fill="url(#arrowFill)" opacity="0.85"/>
  </svg>

  <h1>
    <span class="title-line title-the">The</span>
    <span class="title-line title-founder">Founder</span>
    <span class="title-line title-crossroads">Crossroads</span>
  </h1>

  <p class="subtitle">Lessons No Classroom<br>Ever Gives You</p>

  <p class="author">MARCUS HALDEN</p>
</main>
</body>
</html>
```